Talvora Recovery Massage needs a Website

I'm a Massage Practitioner wanting a website for promotion and bookings with a Blog area and inplementation to my quellbook page https://www.quellbook.example/TalvoraRecoveryMassage , my bookvane Booking page http://my.bookvane.example/bookingpage/a83d2e71-4c05-4b9e-8d12-7f6c0e93b2aa and my CoinDrop account to make payments.
The Venues changes from time to time. In October 2015 it will be the Duskrunner Multisport Globalfinals in Kona Hawaii

Target Market(s)

Sports People participating in targeted Events

Industry/Entity Type

Massage

Number of Pages Required

5+ page

Font styles to use
Other font styles liked:
• Verdana

Colors
3176b5
5db8de
ec1f27
ffffff

Requirements
Must have
• An About page including which events (in this case Duskrunner Multisport Global Finals in Kona, Hawaii in October 2015)
• A page with the Techniques I use
• Inplementation of my Bookvane Booking Page http://my.bookvane.example/bookingpage/a83d2e71-4c05-4b9e-8d12-7f6c0e93b2aa
• Implementation of my Quellbook Page https://www.quellbook.example/TalvoraRecoveryMassage
Nice to have
• Would be great to have a Blog with Pictures Upload ability
• Tried to upload Pictures but it always says that it is a non supported file type, so contact me to send you those informations. More informations about me to be found on http://wellfold-clinic.example/about-us/meet-the-team/tor-haskell-brandt---massage-therapist.html

```html
<!DOCTYPE html>
<html lang="en">
<head>
<meta charset="utf-8">
<title>Talvora Recovery Massage</title>
<link href="https://fonts.googleapis.com/css2?family=Jockey+One&family=Ropa+Sans&family=Open+Sans:wght@400;600&display=swap" rel="stylesheet">
<style>
:root{
  --blue:#3176b5;
  --blue-dark:#2a64a0;
  --sky:#5db8de;
  --red:#ec1f27;
  --white:#ffffff;
  --ink:#555b62;
  --grey-band:#efefef;
  --footer:#2b2b2b;
  --footer-text:#9a9a9a;
}
*{box-sizing:border-box;margin:0;padding:0}
html,body{width:745px;height:1200px;overflow:hidden;background:var(--white)}
body{position:relative;font-family:"Open Sans",Verdana,sans-serif;color:var(--ink)}
.top-band{position:absolute;left:0;top:0;width:745px;height:323px;background:linear-gradient(#3a86cf,var(--blue))}
.site-header{position:absolute;left:62px;top:38px;width:622px;height:63px;background:var(--white);display:flex;align-items:center;justify-content:space-between;padding:0 21px 0 12px}
.brand{display:flex;align-items:center;gap:6px}
.brand-dot{width:20px;height:20px;border-radius:50%;background:var(--sky)}
.brand-name{font-family:"Ropa Sans",sans-serif;font-size:8px;line-height:9px;color:var(--red);width:60px}
.main-nav{display:flex;gap:21px;font-family:"Ropa Sans",sans-serif;font-size:9px;color:#666}
.main-nav .active{color:var(--blue)}
.hero{position:absolute;left:62px;top:101px;width:622px;height:311px;background:linear-gradient(90deg,#2e2e2e 0%,#4a4a44 35%,#8a8270 60%,#b9b48e 100%);box-shadow:0 12px 14px -10px rgba(0,0,0,.35)}
.hero-copy{position:absolute;left:36px;top:38px;color:var(--white)}
.hero-title{font-family:"Jockey One",sans-serif;font-size:44px;line-height:49px;font-weight:400}
.hero-text{font-size:7.5px;line-height:13px;margin-top:14px;width:140px}
.btn{display:inline-block;background:linear-gradient(var(--blue),var(--blue-dark));color:var(--white);border-radius:3px;box-shadow:0 2px 3px rgba(0,0,0,.25)}
.hero-btn{margin-top:13px;padding:10px 12px;font-family:"Jockey One",sans-serif;font-size:12px;letter-spacing:.5px}
.dots{display:flex;gap:6px;margin-top:18px}
.dots span{width:7px;height:7px;border-radius:50%;background:#aaa}
.dots span:first-child{background:var(--blue)}
.welcome{position:absolute;left:62px;top:440px;width:375px}
.section-title{font-family:"Jockey One",sans-serif;color:var(--blue);font-size:25px;line-height:30px;font-weight:400}
.welcome .section-title{max-width:350px;margin-bottom:4px}
.welcome p{font-size:7px;line-height:12.8px;margin-top:12px}
.read-btn{margin-top:17px;padding:0 14px;height:34px;line-height:34px;font-family:"Ropa Sans",sans-serif;font-size:9px}
.video{position:absolute;left:449px;top:492px;width:234px;height:163px;border:2px solid #e6e6e6;background:linear-gradient(135deg,#d6d6d6,#8c8c8c 60%,#5a5a5a)}
.video svg{position:absolute;left:92px;top:56px}
.services{position:absolute;left:0;top:679px;width:745px;height:269px;background:var(--grey-band)}
.services .section-title{text-align:center;margin-top:32px}
.service-list{position:absolute;left:62px;top:84px;display:flex;gap:15px}
.service-card{width:197px;box-shadow:0 14px 12px -10px rgba(0,0,0,.3)}
.service-photo{height:110px}
.service-label{height:37px;line-height:37px;padding-left:11px;background:linear-gradient(#5096d8,var(--blue-dark));color:var(--white);font-family:"Ropa Sans",sans-serif;font-size:15px}
.pricing{position:absolute;left:62px;top:962px}
.price-list{display:flex;gap:12px;margin-top:18px}
.price-card{width:199px;height:101px;background:radial-gradient(circle,#fff 55%,#ececec);text-align:center;padding-top:22px;box-shadow:0 0 3px rgba(0,0,0,.12)}
.price-name{font-family:"Ropa Sans",sans-serif;font-size:15px;line-height:19px;color:#444}
.price-amount{font-family:"Jockey One",sans-serif;font-size:19px;color:var(--blue);margin-top:7px}
.site-footer{position:absolute;left:0;top:1143px;width:745px;height:57px;background:var(--footer)}
.footer-links{position:absolute;left:62px;top:16px;font-family:"Ropa Sans",sans-serif;font-size:7px;line-height:13px;color:var(--footer-text)}
.social{position:absolute;left:570px;top:17px;display:flex;gap:4px}
.social span{width:19px;height:19px;background:#3c3c3c}
</style>
</head>
<body>
<div class="top-band"></div>

<header class="site-header">
  <div class="brand"><span class="brand-dot"></span><span class="brand-name">Talvora Recovery Massage</span></div>
  <nav class="main-nav">
    <span class="active">Massage Research</span><span>Education</span><span>Community Service</span><span>Grants &amp; Contests</span><span>Resources</span><span>Blog</span>
  </nav>
</header>

<section class="hero" role="img" aria-label="Therapist giving a back massage in the treatment room">
  <div class="hero-copy">
    <h1 class="hero-title">Massage<br>Practitioner</h1>
    <p class="hero-text">Tor turned his passion for sport into a passion for helping athletes.</p>
    <span class="btn hero-btn">BOOK NOW</span>
    <div class="dots"><span></span><span></span><span></span></div>
  </div>
</section>

<section class="welcome">
  <h2 class="section-title">Welcome to Talvora Recovery Massage</h2>
  <p>Tor turned his passion for sport into a passion for helping athletes. As a Massage Therapist he helps athletes to perform optimally and recover faster from training and racing. Tor is trained in Swedish, Remedial &amp; Sports Massage, Active Glide Technique (AGT), STRATA Myofascial Release, Halden Technique, Dry Needeling and Lymphatic Drainage.</p>
  <p>With 29 Duskrunner Multisport races under his belt and 3 World Championships, Tor has received a lot of body work through the years. As a result, his focus has been to package his soft tissue skills into a treatment that combines many different techniques to achieve optimal performance and recovery.</p>
  <span class="btn read-btn">Read More</span>
</section>

<div class="video" role="img" aria-label="Video of a massage session at an event tent">
  <svg width="48" height="48" viewBox="0 0 48 48"><circle cx="24" cy="24" r="22" fill="#111" stroke="#fff" stroke-width="3"/><path d="M19 13 L35 24 L19 35 Z" fill="#fff"/></svg>
</div>

<section class="services">
  <h2 class="section-title">Our Services</h2>
  <div class="service-list">
    <div class="service-card"><div class="service-photo" role="img" aria-label="Athlete celebrating at a race finish" style="background:linear-gradient(#6a6a5c,#9a8f7e)"></div><div class="service-label">SPORT MASSAGE</div></div>
    <div class="service-card"><div class="service-photo" role="img" aria-label="Therapist performing myofascial release" style="background:linear-gradient(#7a7566,#c2be9a)"></div><div class="service-label">MYOFASCIAL RELEASE</div></div>
    <div class="service-card"><div class="service-photo" role="img" aria-label="Therapist doing soft tissue work" style="background:linear-gradient(#8b8f92,#c9c7c2)"></div><div class="service-label">SOFT TISSUE WORK</div></div>
  </div>
</section>

<section class="pricing">
  <h2 class="section-title">Pricing</h2>
  <div class="price-list">
    <div class="price-card"><div class="price-name">Sport Deep Tissue<br>Massage</div><div class="price-amount">60 mins$100</div></div>
    <div class="price-card"><div class="price-name">Myofascial<br>Release</div><div class="price-amount">60 mins$120</div></div>
    <div class="price-card"><div class="price-name">Sport Deep Tissue<br>with Active Soft Tissue Work</div><div class="price-amount">60 mins$120</div></div>
  </div>
</section>

<footer class="site-footer">
  <div class="footer-links">Home &nbsp;/&nbsp; Education &nbsp;/&nbsp; Services &nbsp;/&nbsp; Grants &amp; Contests &nbsp;/&nbsp; Blog<br>Copyright © 2015 &nbsp; Talvora Recovery Massage</div>
  <div class="social" aria-label="Social links"><span></span><span></span><span></span><span></span><span></span></div>
</footer>
</body>
</html>
```